Float and wellness centre needs a website refresh

Our float and wellness centre has been operating in Brisbane, Australia for 3 months. Our website is functional and easy to use, but it lacks a compelling visual experience that sells our awesome services to our customers.<br/><br/>We would like a complete redesign of our webpage. It is very important that the redesign considers the page layout for mobile users and the winning design will need to show both a desktop and mobile version of each of the pages listed below.<br/><br/>Out current website can be found at https://www.ommivitalityhaven.com.au/<br/><br/>The winning design will need to provide proposals for redesigning the 4 pages listed below:<br/>Home Page - https://www.ommivitalityhaven.com.au/<br/>Float Page - https://www.ommivitalityhaven.com.au/services/float<br/>Build Gift Card page - https://www.ommivitalityhaven.com.au/giftcard/stepone?location=kelverdale<br/>Booking Page - https://www.ommivitalityhaven.com.au/Calendar/Day?centerId=kelverdale&selectedCategory=FLOAT&date=12/18/2019%2000:00:00%20+10:00&sessionLength=60<br/><br/>We only need the 4 pages listed above as our web developer will use the assets from the above pages to standardize all the other pages in the site. It is very important your proposed pages contain the same information as our current pages so that we can properly see the complete layout.<br/><br/>The Home page must display the business logo in some way. We would like the website to have a white background and for it make tasteful use of color to highlight key features on the pages. Where color is used it should harmonize with the business logo. The website needs to feel bright, simple and relaxing. Our current site does not use images very well and we have had professional photos taken of the center and the float rooms specifically for this website project. You can download these, and the business logo images here: http://ommivitalityhaven.com.au/websiteimages.zip <br/><br/>We have included a few links below to other centers who have pages that we like: <br/><br/>https://www.driftquietlyhere.com/ <br/>https://www.lullnook.com.au/ <br/>https://www.skylinedrift.com.au/<br/>

Industry/Entity Type

Health And Wellness

Number of Pages Required

4 page

Font styles to use
Sans Serif

Colors

Designer to choose colors to be used in the design.

Requirements
Must have
• It is very important your proposed pages contain the same information as our current pages so that we can properly see the complete layout.
• The Home page must display the business logo in some way.
• Where color is used it should harmonize with the business logo.
Nice to have
• The website needs to feel bright, simple and relaxing. Our current site does not use images very well and we have had professional photos taken of the center and the float rooms specifically for this website project. You can download these, and the business logo images here: http://ommivitalityhaven.com.au/websiteimages.zip
Should not have
• Dark pages.

```html
<!DOCTYPE html>
<html lang="en">
<head>
<meta charset="utf-8">
<title>Ommi Vitality Haven</title>
<link rel="stylesheet" href="https://fonts.googleapis.com/css2?family=Poppins:wght@300;400;500;600;700&display=swap">
<style>
:root{
  --teal:#1fb3b8;
  --teal-dark:#15989c;
  --pink-a:#f5576c;
  --pink-b:#e83a66;
  --ink:#333;
  --muted:#8a8a8a;
  --mist:#f3f0ef;
  --night:#2c2c2d;
  --white:#fff;
}
*{box-sizing:border-box;margin:0;padding:0}
html,body{width:1200px;height:3528px;overflow:hidden}
body{font-family:"Poppins",sans-serif;color:var(--ink);background:var(--white);position:relative}
.abs{position:absolute}
section,header,footer{position:absolute;left:0;width:1200px}

/* header */
.site-header{top:0;height:108px;background:var(--white)}
.contact-strip{top:8px;right:28px;font-size:11px;color:var(--teal);display:flex;gap:22px}
.brand{left:28px;top:26px;display:flex;align-items:center;gap:10px}
.brand-dot{width:16px;height:16px;border-radius:50%;background:var(--teal)}
.brand-name{font-size:15px;font-weight:600;color:var(--teal);line-height:1.1;width:110px}
.main-nav{left:330px;top:62px;display:flex;gap:44px;font-size:13px;color:#555}
.btn-login{left:896px;top:54px;width:86px;height:32px;border:1px solid var(--teal);color:var(--teal);font-size:11px;font-weight:600;display:flex;align-items:center;justify-content:center;border-radius:2px}
.btn-book{left:1000px;top:54px;width:118px;height:32px;background:var(--teal);color:var(--white);font-size:11px;font-weight:600;display:flex;align-items:center;justify-content:center;border-radius:2px}

/* hero */
.hero{top:108px;height:484px}
.hero-photo{inset:0;background:linear-gradient(100deg,#c9c7c2 0%,#e6e4df 35%,#f4f6f7 55%,#bfe3f2 75%,#7ec4e6 100%)}
.hero-title{left:136px;top:250px;font-size:46px;font-weight:600;color:var(--white);text-shadow:0 2px 6px rgba(0,0,0,.25)}
.hero-sub{left:136px;top:316px;font-size:16px;color:var(--white);width:300px;line-height:1.4;text-shadow:0 1px 4px rgba(0,0,0,.3)}
.hero-arrow{top:214px}
.hero-dots{left:0;right:0;bottom:18px;display:flex;justify-content:center;gap:8px}
.hero-dots span{width:9px;height:9px;border-radius:50%;background:rgba(255,255,255,.6)}
.hero-dots span.on{background:var(--white)}

/* mission */
.mission{top:592px;height:480px}
.mission-frame{left:88px;top:56px;width:520px;height:324px;background:var(--teal)}
.mission-photo{left:106px;top:70px;width:520px;height:316px;background:linear-gradient(135deg,#efece6,#d9d3c9 60%,#b9b0a2)}
.mission-title{left:770px;top:180px;font-size:40px;font-weight:500}
.mission-text{left:770px;top:240px;width:360px;font-size:13px;line-height:1.65;color:var(--muted)}

/* services */
.services{top:1072px;height:480px;background:var(--mist)}
.section-title{left:0;right:0;text-align:center;font-size:40px;font-weight:500}
.service{top:160px;width:240px;text-align:center}
.service-photo{width:180px;height:180px;border-radius:50%;margin:0 auto;border:6px solid var(--white);box-shadow:0 4px 14px rgba(0,0,0,.12)}
.service-name{font-size:22px;font-weight:500;margin-top:22px}
.service-desc{font-size:11px;color:var(--muted);line-height:1.5;margin-top:4px}
.service-go{width:28px;height:28px;border-radius:50%;background:var(--teal);margin:10px auto 0;display:flex;align-items:center;justify-content:center}

/* hours */
.hours{top:1552px;height:704px}
.hours-sub{left:0;right:0;top:132px;text-align:center;font-size:13px;color:var(--muted)}
.session{left:100px;width:332px;height:150px;background:var(--teal);color:var(--white);text-align:center;padding:10px}
.session-inner{border:1px solid rgba(255,255,255,.7);height:100%;display:flex;flex-direction:column;justify-content:center}
.session-name{font-size:22px;font-weight:500}
.session-time{font-size:12px;opacity:.9}
.hours-photo{left:460px;top:176px;width:652px;height:492px;background:linear-gradient(160deg,#eef0f0,#dfe2e2 50%,#b8c7cf 80%,#3f6e8c)}

/* pricing */
.pricing{top:2256px;height:544px;background:var(--mist)}
.price-card{top:124px;width:215px;height:260px;background:var(--white);box-shadow:0 6px 16px rgba(0,0,0,.08)}
.price-top{position:absolute;left:0;top:0}
.price-length{position:absolute;left:0;right:0;top:40px;text-align:center;color:var(--white);font-size:34px;font-weight:700;line-height:1}
.price-item{position:absolute;left:0;right:0;top:80px;text-align:center;color:var(--white);font-size:20px;font-weight:500}
.price-amount{position:absolute;left:0;right:0;top:200px;text-align:center;color:var(--teal);font-size:24px;font-weight:600}
.member-title{left:0;right:0;top:420px;text-align:center;font-size:22px;font-weight:600}
.member-rate{left:0;right:0;top:452px;text-align:center;font-size:13px;color:var(--muted)}
.member-btn{left:452px;top:480px;width:296px;height:34px;background:var(--teal);color:var(--white);font-size:12px;font-weight:500;display:flex;align-items:center;justify-content:center}

/* contact */
.contact{top:2800px;height:400px}
.map{left:100px;top:60px;width:448px;height:300px;background:linear-gradient(135deg,#eef1ec,#e3e8e2 50%,#d7e6f0)}
.contact-title{left:588px;top:64px;font-size:28px;font-weight:500}
.field{height:34px;border:1px solid #ccc;font-size:11px;color:#999;padding:8px 10px}
.send-btn{left:1036px;top:322px;width:72px;height:30px;background:var(--teal);color:var(--white);font-size:11px;font-weight:600;display:flex;align-items:center;justify-content:center}

/* footer */
.site-footer{top:3200px;height:328px;background:var(--night);color:#cfcfcf}
.foot-brand{left:90px;top:44px;width:140px;display:flex;flex-direction:column;align-items:flex-start;gap:10px}
.foot-brand .brand-dot{width:56px;height:56px}
.foot-brand .brand-name{color:var(--white);font-size:16px}
.foot-col{top:44px;font-size:11px;line-height:1.7}
.foot-col h4{font-size:13px;font-weight:600;color:var(--white);margin-bottom:10px}
.foot-line{display:flex;align-items:flex-start;gap:8px;margin-bottom:8px}
.foot-brand-small{left:872px;top:44px;display:flex;align-items:center;gap:8px;font-size:15px;font-weight:600;color:var(--white)}
.follow{left:872px;top:104px;font-size:13px;font-weight:600;color:var(--white)}
.social{left:872px;top:134px;display:flex;gap:10px}
.social span{width:16px;height:16px;border-radius:50%;background:#cfcfcf}
.copyright{left:0;right:0;bottom:12px;text-align:center;font-size:10px;color:#999}
</style>
</head>
<body>

<header class="site-header">
  <div class="abs contact-strip"><span>info@ommivitalityhaven.com.au</span><span>(07) 3000 1234</span></div>
  <div class="abs brand"><span class="brand-dot"></span><span class="brand-name">Ommi Vitality Haven</span></div>
  <nav class="abs main-nav"><span>Home</span><span>Float</span><span>IR Sauna</span><span>mhBOT</span><span>Thermal Mat</span><span>Gift Cards</span></nav>
  <div class="abs btn-login">LOGIN</div>
  <div class="abs btn-book">BOOK NOW</div>
</header>

<section class="hero">
  <div class="abs hero-photo" role="img" aria-label="Float room with open white float pod filled with blue-lit water beside a glass shower"></div>
  <svg class="abs hero-arrow" style="left:22px" width="20" height="40" viewBox="0 0 20 40"><path d="M16 4 L4 20 L16 36" fill="none" stroke="#fff" stroke-width="3"/></svg>
  <svg class="abs hero-arrow" style="right:22px" width="20" height="40" viewBox="0 0 20 40"><path d="M4 4 L16 20 L4 36" fill="none" stroke="#fff" stroke-width="3"/></svg>
  <h1 class="abs hero-title">Ommi Vitality Haven</h1>
  <p class="abs hero-sub">Our mission is to provide a purpose-built space for our clients to relax.</p>
  <div class="abs hero-dots"><span class="on"></span><span></span><span></span></div>
</section>

<section class="mission">
  <div class="abs mission-frame"></div>
  <div class="abs mission-photo" role="img" aria-label="Treatment room with a massage bed and potted plant"></div>
  <h2 class="abs mission-title">Our Mission</h2>
  <p class="abs mission-text">Our mission is to provide a purpose-built space for our clients to relax, recover and optimise their health. Ommi Vitality Haven offers Flotation Therapy, Mild Hyperbaric Oxygen Therapy (mhBOT), Infrared Sauna and Thermal Mat sessions.</p>
</section>

<section class="services">
  <h2 class="abs section-title" style="top:52px">Our Services</h2>
  <div class="abs service" style="left:86px">
    <div class="service-photo" role="img" aria-label="Open float pod glowing blue" style="background:radial-gradient(circle at 45% 55%,#c8eef7,#6fc3e0 55%,#3f6f86)"></div>
    <div class="service-name">Float</div>
    <div class="service-desc">Relax, recharge and replenish<br>your body.</div>
    <div class="service-go"><svg width="12" height="12" viewBox="0 0 12 12"><path d="M2 6h8M7 3l3 3-3 3" fill="none" stroke="#fff" stroke-width="1.6"/></svg></div>
  </div>
  <div class="abs service" style="left:338px">
    <div class="service-photo" role="img" aria-label="Hyperbaric oxygen chamber in a room" style="background:radial-gradient(circle at 50% 50%,#8e8a86,#4d4a48 60%,#2d2b2a)"></div>
    <div class="service-name">mhBOT</div>
    <div class="service-desc">Mild Hyperbaric Oxygen Therapy,<br>oxygen-assisted healing.</div>
    <div class="service-go"><svg width="12" height="12" viewBox="0 0 12 12"><path d="M2 6h8M7 3l3 3-3 3" fill="none" stroke="#fff" stroke-width="1.6"/></svg></div>
  </div>
  <div class="abs service" style="left:590px">
    <div class="service-photo" role="img" aria-label="Infrared sauna cabin with warm pink light" style="background:radial-gradient(circle at 50% 50%,#f6c6d8,#e07aa6 55%,#8a3e62)"></div>
    <div class="service-name">IR Sauna</div>
    <div class="service-desc">Enhance sleep and detox with our<br>Infrared Sauna.</div>
    <div class="service-go"><svg width="12" height="12" viewBox="0 0 12 12"><path d="M2 6h8M7 3l3 3-3 3" fill="none" stroke="#fff" stroke-width="1.6"/></svg></div>
  </div>
  <div class="abs service" style="left:842px">
    <div class="service-photo" role="img" aria-label="Client resting on a heated crystal mat" style="background:radial-gradient(circle at 50% 50%,#e7b98f,#b0734a 55%,#5a3520)"></div>
    <div class="service-name">Thermal Mat</div>
    <div class="service-desc">Far Infrared Rays, Negative Ions<br>and heated crystals.</div>
    <div class="service-go"><svg width="12" height="12" viewBox="0 0 12 12"><path d="M2 6h8M7 3l3 3-3 3" fill="none" stroke="#fff" stroke-width="1.6"/></svg></div>
  </div>
</section>

<section class="hours">
  <h2 class="abs section-title" style="top:72px">Hours</h2>
  <p class="abs hours-sub">We open earlier and stay open longer, just for you.</p>
  <div class="abs session" style="top:176px"><div class="session-inner"><div class="session-name">Early Sessions</div><div class="session-time">6AM – 9AM</div></div></div>
  <div class="abs session" style="top:346px"><div class="session-inner"><div class="session-name">Normal Sessions</div><div class="session-time">9AM – 5PM</div></div></div>
  <div class="abs session" style="top:516px"><div class="session-inner"><div class="session-name">Late Sessions</div><div class="session-time">5PM – 10PM</div></div></div>
  <div class="abs hours-photo" role="img" aria-label="Reception area with blue sofa, white counter and hanging plants"></div>
</section>

<section class="pricing">
  <h2 class="abs section-title" style="top:52px">Pricing</h2>
  <svg width="0" height="0" style="position:absolute"><defs><linearGradient id="pinkFade" x1="0" y1="0" x2="0" y2="1"><stop offset="0" stop-color="#f5576c"/><stop offset="1" stop-color="#e83a66"/></linearGradient></defs></svg>
  <div class="abs price-card" style="left:100px">
    <svg class="price-top" width="215" height="170" viewBox="0 0 215 170"><path d="M0 0H215V130Q107 180 0 130Z" fill="url(#pinkFade)"/></svg>
    <div class="price-length">60 min</div><div class="price-item">Float Tank</div><div class="price-amount">$65.00</div>
  </div>
  <div class="abs price-card" style="left:352px">
    <svg class="price-top" width="215" height="170" viewBox="0 0 215 170"><path d="M0 0H215V130Q107 180 0 130Z" fill="url(#pinkFade)"/></svg>
    <div class="price-length">30 min</div><div class="price-item">IR Sauna</div><div class="price-amount">$40.00</div>
  </div>
  <div class="abs price-card" style="left:604px">
    <svg class="price-top" width="215" height="170" viewBox="0 0 215 170"><path d="M0 0H215V130Q107 180 0 130Z" fill="url(#pinkFade)"/></svg>
    <div class="price-length">45 min</div><div class="price-item">min Thermal Mat</div><div class="price-amount">$45.00</div>
  </div>
  <div class="abs price-card" style="left:856px">
    <svg class="price-top" width="215" height="170" viewBox="0 0 215 170"><path d="M0 0H215V130Q107 180 0 130Z" fill="url(#pinkFade)"/></svg>
    <div class="price-length">60 min</div><div class="price-item">mhBOT</div><div class="price-amount">$70.00</div>
  </div>
  <div class="abs member-title">Membership*</div>
  <div class="abs member-rate">$20.00 PER MONTH</div>
  <div class="abs member-btn">$20 OFF EVERY BOOKING</div>
</section>

<section class="contact">
  <div class="abs map" role="img" aria-label="Street map showing the centre location"></div>
  <svg class="abs" style="left:300px;top:170px" width="24" height="34" viewBox="0 0 24 34"><path d="M12 0C5 0 0 5 0 12c0 9 12 22 12 22s12-13 12-22C24 5 19 0 12 0z" fill="#e83a4a"/><circle cx="12" cy="12" r="4.5" fill="#fff"/></svg>
  <h2 class="abs contact-title">Get In Touch</h2>
  <div class="abs field" style="left:588px;top:120px;width:248px">Name</div>
  <div class="abs field" style="left:852px;top:120px;width:256px">Email</div>
  <div class="abs field" style="left:588px;top:166px;width:248px">Phone</div>
  <div class="abs field" style="left:852px;top:166px;width:256px">Address</div>
  <div class="abs field" style="left:588px;top:212px;width:520px;height:100px">Message</div>
  <div class="abs send-btn">SEND</div>
</section>

<footer class="site-footer">
  <div class="abs foot-brand"><span class="brand-dot"></span><span class="brand-name">Ommi Vitality Haven</span></div>
  <div class="abs foot-col" style="left:268px;width:230px">
    <h4>Ommi Vitality Haven</h4>
    <div class="foot-line"><svg width="10" height="14" viewBox="0 0 24 34"><path d="M12 0C5 0 0 5 0 12c0 9 12 22 12 22s12-13 12-22C24 5 19 0 12 0z" fill="#1fb3b8"/></svg><span>Unit 4/12 Harbour Rd,<br>Kelverdale QLD 4500</span></div>
    <div class="foot-line"><svg width="12" height="10" viewBox="0 0 12 10"><rect x=".5" y=".5" width="11" height="9" fill="none" stroke="#1fb3b8"/><path d="M.5 .5L6 5l5.5-4.5" fill="none" stroke="#1fb3b8"/></svg><span>info@ommivitalityhaven.com.au</span></div>
    <div class="foot-line"><svg width="12" height="12" viewBox="0 0 12 12"><path d="M2 1l2.5 0 1 3-1.5 1c.7 1.4 1.6 2.3 3 3l1-1.5 3 1V11C5 11 1 7 1 2z" fill="#1fb3b8"/></svg><span>(07) 3000 1234</span></div>
  </div>
  <div class="abs foot-col" style="left:540px">
    <h4>Sessions Hours</h4>
    <div>Early Sessions</div><div style="margin-bottom:6px">6AM – 9AM</div>
    <div>Normal Sessions</div><div style="margin-bottom:6px">9AM – 5PM</div>
    <div>Late Sessions</div><div>5PM – 10PM</div>
  </div>
  <div class="abs foot-col" style="left:708px">
    <h4>Other Links</h4>
    <div>Booking Policy</div><div>Membership Policy</div><div>Privacy Policy</div><div>Cancellation Policy</div><div>FAQ</div><div>Website</div>
  </div>
  <div class="abs foot-brand-small"><span class="brand-dot" style="width:22px;height:22px"></span>OMMI VITALITY HAVEN</div>
  <div class="abs follow">Follow Us</div>
  <div class="abs social"><span></span><span></span></div>
  <div class="abs copyright">© 2020 Ommi Vitality Haven. All Rights Reserved.</div>
</footer>

</body>
</html>
```